Bref créative
Brochure for Professional Services Firm
Brightfen Partners
We need a great design for a brochure to be used as marketing collateral at tradeshows and for general marketing purposes. Our website is brightfenpartners.example to get additional information. We generally work with oilfield service companies.
Consulting
Corporate, professional.
===========Update==========
Requirement : Trifold
Our logo files.
Here is a sample presentation we currently use to market our services.
Some stock photos we have.
stock photos.
stock photo.

```html
<!DOCTYPE html>
<html lang="en">
<head>
<meta charset="utf-8">
<title>Brightfen Partners – Trifold Brochure</title>
<link rel="stylesheet" href="https://fonts.googleapis.com/css2?family=Open+Sans:wght@400;600;700&family=Montserrat:wght@600;700&display=swap">
<style>
  :root{
    --page-bg:#e9e8e5;
    --paper:#ffffff;
    --ink:#3a3f46;
    --ink-soft:#5d646d;
    --accent:#2a7ab8;
    --band:#2c333c;
    --night-top:#3b4a5c;
    --night-bottom:#141a22;
    --sky-warm:#d9d2c4;
    --sky-cool:#8ea0b2;
    --rule:#c9ced4;
  }
  *{box-sizing:border-box;margin:0;padding:0}
  html,body{width:1200px;height:708px;overflow:hidden}
  body{background:var(--page-bg);font-family:"Open Sans",Arial,sans-serif;color:var(--ink);position:relative}

  .spread{position:absolute;top:134px;width:570px;height:440px;box-shadow:0 4px 14px rgba(0,0,0,.18);overflow:hidden}
  .spread--inside{left:20px;background:var(--paper)}
  .spread--outside{left:610px;background:linear-gradient(180deg,var(--night-top),var(--night-bottom))}

  /* inside */
  .hero{position:absolute;left:0;top:0;width:570px;height:108px;background:linear-gradient(180deg,var(--sky-warm),var(--sky-cool))}
  .services-band{position:absolute;left:0;top:108px;width:570px;height:28px;background:var(--band);display:flex;align-items:center;justify-content:center}
  .services-band h1{font-family:Montserrat,Arial,sans-serif;font-weight:700;font-size:15px;letter-spacing:4px;color:#fff}
  .tagline{position:absolute;left:0;top:142px;width:570px;text-align:center;font-size:10.5px;font-weight:600;color:var(--ink)}
  .columns{position:absolute;left:14px;top:166px;width:542px;height:262px;display:flex;gap:14px}
  .column{flex:1;position:relative}
  .column h2{font-size:8.5px;font-weight:700;color:var(--accent);margin-bottom:5px}
  .column p{font-size:6.4px;line-height:1.5;color:var(--ink-soft);margin-bottom:5px}
  .column h3{font-size:6.6px;font-weight:700;color:var(--ink);margin-bottom:3px}
  .column ul{list-style:none;font-size:6.4px;line-height:1.6;color:var(--ink-soft)}
  .column li::before{content:"• ";color:var(--accent)}
  .web{position:absolute;left:0;bottom:4px;font-size:9px;font-weight:600;color:var(--ink)}
  .field-photo{position:absolute;left:0;bottom:0;width:100%;height:90px;background:linear-gradient(180deg,#b9c6d3,#7f8e76)}
  .brand{display:flex;align-items:center;gap:6px}
  .brand-mark{width:18px;height:18px;background:var(--accent)}
  .brand-name{font-family:"Open Sans",Arial,sans-serif;font-weight:700;font-size:14px;letter-spacing:2px;color:var(--band)}
  .column .brand{position:absolute;left:0;bottom:4px}

  /* outside */
  .panel{position:absolute;top:0;width:190px;height:440px}
  .panel--about{left:0;padding:22px 16px}
  .panel--back{left:190px}
  .panel--cover{left:380px}
  .panel--about h2{font-size:10px;font-weight:700;color:#fff;margin-bottom:6px}
  .panel--about p{font-size:6.4px;line-height:1.55;color:#d5dbe2;margin-bottom:6px}
  .dusk-photo{position:absolute;left:0;bottom:0;width:380px;height:190px;background:linear-gradient(180deg,rgba(150,165,180,.55),#0f141a)}
  .cover-photo{position:absolute;left:0;top:150px;width:190px;height:290px;background:linear-gradient(180deg,#6e8196,#10161d)}
  .contact{position:absolute;left:16px;top:40px;font-size:6.4px;line-height:1.6;color:#d5dbe2}
  .panel--cover .brand{position:absolute;left:22px;top:60px}
  .panel--cover .brand-name{color:#fff}
  .cover-web{position:absolute;right:14px;bottom:12px;font-size:7px;color:#d5dbe2}
  .fold{position:absolute;top:0;width:1px;height:440px;background:rgba(255,255,255,.08)}
</style>
</head>
<body>

<section class="spread spread--inside" aria-label="Brochure inside spread">
  <div class="hero" role="img" aria-label="Silhouettes of four businessmen in front of oil pumpjacks at sunset"></div>
  <div class="services-band"><h1>SERVICES</h1></div>
  <p class="tagline">Boutique financial and transaction advisory services for small and mid-market companies.</p>

  <div class="columns">
    <article class="column">
      <h2>Transaction Advisory Services</h2>
      <p>We guide owners through acquisitions, divestitures and recapitalizations with clear analysis and steady counsel from first review to closing.</p>
      <h3>Our Transaction Services include:</h3>
      <ul>
        <li>Buy-side due diligence</li>
        <li>Quality of earnings reviews</li>
        <li>Sell-side preparation</li>
        <li>Working capital analysis</li>
        <li>Purchase price support</li>
      </ul>
      <span class="web">www.brightfenpartners.example</span>
    </article>

    <article class="column">
      <h2>Financial Advisory Services</h2>
      <p>Our advisors help management teams strengthen reporting, forecasting and controls so every decision rests on reliable numbers.</p>
      <ul>
        <li>Budgeting and forecasting</li>
        <li>Cash flow planning</li>
        <li>Lender reporting</li>
        <li>Process improvement</li>
      </ul>
      <div class="field-photo" role="img" aria-label="Oil pumpjack in an open field under a blue sky"></div>
    </article>

    <article class="column">
      <h2>Transitional CFO Services</h2>
      <p>When a finance leader departs or growth outpaces the team, we step in with experienced interim leadership.</p>
      <h3>Interim financial leadership during change</h3>
      <ul>
        <li>Monthly close oversight</li>
        <li>Board reporting</li>
        <li>Audit readiness</li>
      </ul>
      <div class="brand"><span class="brand-mark"></span><span class="brand-name">BRIGHTFEN</span></div>
    </article>
  </div>
</section>

<section class="spread spread--outside" aria-label="Brochure outside spread">
  <div class="dusk-photo" role="img" aria-label="Oil pumpjacks silhouetted against a dusk sky"></div>

  <div class="panel panel--about">
    <h2>About Us</h2>
    <p>Brightfen Partners provides financial and transaction advisory services to small and mid-market companies, with deep experience in oilfield services.</p>
    <p>Our team combines hands-on operating knowledge with rigorous analysis to help clients grow, transact and plan with confidence.</p>
    <p>We work alongside owners and managers as trusted advisors, delivering practical answers on schedule.</p>
  </div>

  <div class="panel panel--back">
    <div class="contact">
      1200 Meridian Avenue, Suite 400<br>
      Houston, TX 77002<br>
      info@brightfenpartners.example
    </div>
  </div>

  <div class="panel panel--cover">
    <div class="cover-photo" role="img" aria-label="Two oilfield workers in hard hats silhouetted beside a pumpjack at sunset"></div>
    <div class="brand"><span class="brand-mark"></span><span class="brand-name">BRIGHTFEN</span></div>
    <span class="cover-web">www.brightfenpartners.example</span>
  </div>

  <span class="fold" style="left:190px"></span>
  <span class="fold" style="left:380px"></span>
</section>

</body>
</html>
```